Need powerpoint template for our e-assessment company

We need a powerpoint template for our e-assessment company. We develop and offer a state-of-the-art web-based e-assessment platform.

Our company name is Lumora, which reflects our connection to our cloud-based solution. The lumora cloud is also the highest cloud there is, located at 6-12 km height. This reflects our high ambitions.

We would like a front page, a content page and a back page.

Preferrable we would like a template for both Microsoft Powerpoint and Apple Keynote.

Our main colors are orange (#FF6600) and blue (#70abe4) with grey as secondary color.

The design should reflect:

- Secure
- Modern
- Flexible
- Playful
- Innovative
Updates

Hello,

I have uploaded a new image that shows the logo used in different settings. This gives an impression on how we use our brand. 

For our e-assessment application we are using a design style called flat UI design. This is a minimalistic design principle. We want the powerpoint template to be simple, yet professional.

Industry/Entity Type

It Company

Requirements
Must have
• Font: Myriad or Helvetica Neue

(#FF6600)
(#70abe4)
Nice to have
• The design should be clean and simple.
Should not have
• It should not be a color-bomb. It should not be too corporate (i.e. business people in suit having meetings)

```html
<!DOCTYPE html>
<html lang="en">
<head>
<meta charset="utf-8">
<title>Lumora – Presentation Template</title>
<link rel="stylesheet" href="https://fonts.googleapis.com/css2?family=Roboto:wght@300;400;700&display=swap">
<style>
  :root {
    --orange: #f26a21;
    --white: #ffffff;
    --ink: #555555;
    --ink-dark: #3a3a3a;
    --text-grey: #8a8a8a;
    --stage: #000000;
    --footer: #222222;
    --chevron: #3b3b3b;
    --frame: #e6e6e6;
  }
  * { margin: 0; padding: 0; box-sizing: border-box; }
  html, body {
    width: 1200px; height: 910px; overflow: hidden;
    background: var(--stage);
    font-family: "Roboto", "Helvetica Neue", Arial, sans-serif;
  }
  .slide {
    position: absolute; width: 575px; height: 431px; overflow: hidden;
  }
  .slide--cover { left: 24px; top: 23px; background: var(--white); }
  .slide--back { left: 611px; top: 23px; background: var(--orange); }
  .slide--text { left: 24px; top: 466px; background: var(--white); }
  .slide--media { left: 611px; top: 466px; background: var(--white); }

  /* cover */
  .side-bar { position: absolute; left: 0; width: 30px; background: var(--orange); }
  .side-bar--top { top: 0; height: 88px; }
  .side-bar--mid { top: 126px; height: 171px; }
  .side-bar--low { top: 334px; height: 97px; }
  .brand { position: absolute; display: flex; align-items: center; }
  .brand__dot { border-radius: 50%; flex: none; }
  .brand__name { font-weight: 300; line-height: 1; }
  .cover-brand { left: 183px; top: 172px; }
  .cover-brand .brand__dot { width: 74px; height: 74px; background: var(--orange); margin-right: 20px; }
  .cover-brand .brand__name { font-size: 56px; color: var(--ink); }
  .title-block { position: absolute; left: 0; right: 0; text-align: center; }
  .title-block__title { font-weight: 300; font-size: 33px; line-height: 1; }
  .title-block__sub { font-size: 13px; line-height: 17px; margin-top: 10px; }
  .slide--cover .title-block { top: 272px; left: 30px; }
  .slide--cover .title-block__title { color: var(--ink); }
  .slide--cover .title-block__sub { color: var(--text-grey); }

  /* back */
  .back-brand { left: 0; right: 0; top: 121px; flex-direction: column; }
  .back-brand .brand__dot { width: 92px; height: 92px; background: var(--white); }
  .back-brand .brand__name { font-size: 66px; color: var(--white); margin-top: 10px; }
  .slide--back .title-block { top: 298px; }
  .slide--back .title-block__title { color: var(--ink-dark); }
  .slide--back .title-block__sub { color: var(--ink-dark); }

  /* content header & footer */
  .header {
    position: absolute; left: 0; top: 0; width: 100%; height: 54px;
    background: var(--orange); display: flex; align-items: center;
  }
  .header__chevron { position: absolute; left: 0; top: 0; }
  .header__title { color: var(--white); font-size: 24px; font-weight: 400; margin-left: 34px; }
  .header-brand { right: 20px; top: 10px; }
  .header-brand .brand__dot { width: 36px; height: 36px; background: var(--white); margin-right: 6px; }
  .header-brand .brand__name { font-size: 30px; color: var(--white); }
  .footer-rule { position: absolute; left: 0; bottom: 27px; width: 100%; height: 3px; background: var(--orange); }
  .footer {
    position: absolute; left: 0; bottom: 0; width: 100%; height: 27px;
    background: var(--footer); color: var(--white); font-size: 12px;
    text-align: right; padding-right: 16px; line-height: 27px;
  }

  /* body text */
  .copy { position: absolute; font-size: 11px; line-height: 17px; color: var(--text-grey); white-space: nowrap; }
  .copy__heading { color: var(--orange); font-weight: 700; font-size: 11.5px; }
  .photo {
    position: absolute; left: 305px; width: 247px; height: 131px;
    border: 3px solid var(--frame);
    background: linear-gradient(160deg, #b9d3ea 0%, #c6a487 38%, #9a5a3e 62%, #6f7d4a 100%);
  }
</style>
</head>
<body>

<section class="slide slide--cover">
  <div class="side-bar side-bar--top"></div>
  <div class="side-bar side-bar--mid"></div>
  <div class="side-bar side-bar--low"></div>
  <div class="brand cover-brand"><span class="brand__dot"></span><span class="brand__name">lumora</span></div>
  <div class="title-block">
    <h1 class="title-block__title">Project Title here</h1>
    <p class="title-block__sub">Subtext here Subtext here&nbsp; Subtext here Subtext here<br>Subtext here Subtext here</p>
  </div>
</section>

<section class="slide slide--back">
  <div class="brand back-brand"><span class="brand__dot"></span><span class="brand__name">lumora</span></div>
  <div class="title-block">
    <h1 class="title-block__title">Project Title here</h1>
    <p class="title-block__sub">Subtext here Subtext here&nbsp; Subtext here Subtext here<br>Subtext here Subtext here</p>
  </div>
</section>

<section class="slide slide--text">
  <header class="header">
    <svg class="header__chevron" width="20" height="54" viewBox="0 0 20 54"><polygon points="0,0 20,27 0,54" fill="var(--chevron)"/></svg>
    <h2 class="header__title">Project Title here</h2>
    <div class="brand header-brand"><span class="brand__dot"></span><span class="brand__name">lumora</span></div>
  </header>
  <div class="copy" style="left:37px;top:76px">
    Lorem ipsum dolor text Lorem ipsum dolor text<br>Lorem ipsum dolor text Lorem ipsum dolor text<br>Lorem ipsum dolor text Lorem ipsum dolor text<br>Lorem ipsum dolor text Lorem ipsum dolor text<br>Lorem ipsum dolor text Lorem ipsum dolor text<br>Lorem ipsum dolor text Lorem ipsum dolor text<br>Lorem ipsum dolor text Lorem ipsum dolor text<br>Lorem ipsum dolor text Lorem ipsum dolor text
  </div>
  <div class="copy" style="left:37px;top:231px">
    Lorem ipsum dolor text Lorem ipsum dolor text<br>Lorem ipsum dolor text Lorem ipsum dolor text<br>Lorem ipsum dolor text Lorem ipsum dolor text<br>Lorem ipsum dolor text Lorem ipsum dolor text<br>Lorem ipsum dolor text Lorem ipsum dolor text<br>Lorem ipsum dolor text Lorem ipsum dolor text<br>Lorem ipsum dolor text Lorem ipsum dolor text<br>Lorem ipsum dolor text Lorem ipsum dolor text
  </div>
  <div class="copy" style="left:318px;top:76px">
    Lorem ipsum dolor text Lorem ipsum dolor text<br>Lorem ipsum dolor text Lorem ipsum dolor text<br>Lorem ipsum dolor text Lorem ipsum dolor text<br>Lorem ipsum dolor text Lorem ipsum dolor text<br>Lorem ipsum dolor text Lorem ipsum dolor text<br>Lorem ipsum dolor text Lorem ipsum dolor text<br>Lorem ipsum dolor text Lorem ipsum dolor text<br>Lorem ipsum dolor text Lorem ipsum dolor text
  </div>
  <div class="copy" style="left:318px;top:231px">
    Lorem ipsum dolor text Lorem ipsum dolor text<br>Lorem ipsum dolor text Lorem ipsum dolor text<br>Lorem ipsum dolor text Lorem ipsum dolor text<br>Lorem ipsum dolor text Lorem ipsum dolor text<br>Lorem ipsum dolor text Lorem ipsum dolor text<br>Lorem ipsum dolor text Lorem ipsum dolor text<br>Lorem ipsum dolor text Lorem ipsum dolor text<br>Lorem ipsum dolor text Lorem ipsum dolor text
  </div>
  <div class="footer-rule"></div>
  <footer class="footer">Copyright text here</footer>
</section>

<section class="slide slide--media">
  <header class="header">
    <svg class="header__chevron" width="20" height="54" viewBox="0 0 20 54"><polygon points="0,0 20,27 0,54" fill="var(--chevron)"/></svg>
    <h2 class="header__title">Project Title here</h2>
    <div class="brand header-brand"><span class="brand__dot"></span><span class="brand__name">lumora</span></div>
  </header>
  <div class="copy" style="left:37px;top:76px">
    <span class="copy__heading">Lorem ipsum dolor text</span><br>Lorem ipsum dolor text Lorem ipsum dolor text<br>Lorem ipsum dolor text Lorem ipsum dolor text<br>Lorem ipsum dolor text Lorem ipsum dolor text<br>Lorem ipsum dolor text Lorem ipsum dolor text<br>Lorem ipsum dolor text Lorem ipsum dolor text<br>Lorem ipsum dolor text Lorem ipsum dolor text<br>Lorem ipsum dolor text
  </div>
  <div class="copy" style="left:37px;top:231px">
    <span class="copy__heading">Lorem ipsum dolor text</span><br>Lorem ipsum dolor text Lorem ipsum dolor text<br>Lorem ipsum dolor text Lorem ipsum dolor text<br>Lorem ipsum dolor text Lorem ipsum dolor text<br>Lorem ipsum dolor text Lorem ipsum dolor text<br>Lorem ipsum dolor text Lorem ipsum dolor text<br>Lorem ipsum dolor text Lorem ipsum dolor text<br>Lorem ipsum dolor text Lorem ipsum dolor
  </div>
  <div class="photo" style="top:79px" role="img" aria-label="Photo of a smiling man standing outside a brick house"></div>
  <div class="photo" style="top:233px" role="img" aria-label="Photo of a smiling man standing outside a brick house"></div>
  <div class="footer-rule"></div>
  <footer class="footer">Copyright text here</footer>
</section>

</body>
</html>
```